Graphic Design Set for Banner Ads - Sizes and Specs for Pixmora

We need a set of 6 ads of the following sizes created for Pixmora:

Medium rectangle: 300×250
Leaderboard: 728×90
Wide skyscraper: 160×600
Large rectangle: 300x600
Mobile leaderboard: 320×50

Here are the Formatting Guidelines (WEB ADS): https://help.pixmora.example/hc/en-us/articles/583920147-Ad-Content-and-Format-Guidelines

Here is the website: https://valmiraliving.example/

Here are some words for the ad - feel free to use creative liberties if you have something better or need less words.

1. The Future of Aging is Here

2. Dementia At-Home Care

3. Benefits of an Assisted Living from the Privacy of Your Home - link to

4. Idaho's New Senior Care Option

5. The Security of Senior Living from the Comfort of Your Home

I have the images for all website photos, if you need more images, please let me know.

Target Market(s)

Women age 55+

Industry/Entity Type

Graphic Design

Requirements
Must have
• Incorporate website imagery as much as possible
Should not have
• a feeling of helplessness, old, etc.

```html
<!DOCTYPE html>
<html lang="en">
<head>
<meta charset="utf-8">
<title>Valmira Living – Banner Ad Set</title>
<link href="https://fonts.googleapis.com/css2?family=Alegreya:wght@400;700&family=Source+Sans+3:wght@300;400;600&display=swap" rel="stylesheet">
<style>
  :root{
    --cream:#fbf6ea;
    --gold:#f4d99a;
    --gold-line:#f0d9a3;
    --gold-ink:#b8923d;
    --ink:#2f3332;
    --mint:#b7d9d1;
    --sage:#a1c3b3;
    --rose:#d3ab97;
    --mint-2:#bad9d3;
    --mint-3:#b9dad6;
    --sky:#9dc6df;
    --serif:'Alegreya', Georgia, serif;
    --sans:'Source Sans 3', Arial, sans-serif;
  }
  *{box-sizing:border-box;margin:0;padding:0}
  html,body{width:1200px;height:1200px;overflow:hidden}
  body{
    background:radial-gradient(ellipse at 50% 45%,#f7f8f8 0%,#e9ebec 55%,#d3d7d9 100%);
    font-family:var(--sans);color:var(--ink);position:relative;
  }

  /* variants shared by every stack */
  .v1{--i:0;--frame:var(--mint);--photo:linear-gradient(180deg,#6f7a6a 0%,#46513f 34%,#8f9ca2 48%,#b8b8b0 78%,#cbb9a0 100%);z-index:6}
  .v2{--i:1;--frame:var(--sage);--photo:linear-gradient(135deg,#2f2d2b 0%,#6c6660 50%,#c9c2b8 100%);z-index:5}
  .v3{--i:2;--frame:var(--rose);--photo:linear-gradient(135deg,#4a2a14 0%,#9a5b2a 50%,#e1b07a 100%);z-index:4}
  .v4{--i:3;--frame:var(--mint-2);--photo:linear-gradient(135deg,#5f6a5a 0%,#a89f92 55%,#e9e3d8 100%);z-index:3}
  .v5{--i:4;--frame:var(--mint-3);--photo:linear-gradient(135deg,#3a3734 0%,#7c746c 100%);z-index:2}
  .v6{--i:5;--frame:var(--sky);--photo:linear-gradient(180deg,#8fb6dc 0%,#3f6f9a 45%,#2f5a3e 60%,#5f93c2 100%);z-index:1}

  .ad{position:absolute;background:var(--frame);box-shadow:0 2px 6px rgba(0,0,0,.22);overflow:hidden}
  .ad > *{position:absolute}
  .photo{background:var(--photo)}
  .panel{background:var(--cream)}
  .brand{font-family:var(--sans);font-weight:300;color:var(--ink);letter-spacing:.04em;text-align:center;line-height:1}
  .headline{font-family:var(--serif);font-weight:400;color:var(--ink);line-height:1.1}
  .url{font-family:var(--sans);color:var(--ink)}
  .btn{background:var(--gold);color:#5c4a22;font-family:var(--sans);text-align:center;border-radius:2px}

  /* leaderboard 728x90 */
  .leaderboard{width:582px;height:72px;left:calc(202px + var(--i)*24px);top:calc(134px + var(--i)*24px)}
  .leaderboard .brand-cell{left:4px;top:3px;width:110px;height:66px;display:flex;align-items:center;justify-content:center}
  .leaderboard .brand{font-size:15px;color:var(--gold-ink)}
  .leaderboard .photo{left:114px;top:3px;width:108px;height:66px}
  .leaderboard .accent{left:222px;top:3px;width:8px;height:66px;background:var(--gold-line)}
  .leaderboard .copy{left:230px;top:3px;width:322px;height:66px}
  .leaderboard .headline{position:absolute;left:12px;top:4px;font-size:23px;letter-spacing:.02em;white-space:nowrap}
  .leaderboard .url{position:absolute;left:12px;bottom:7px;font-size:12px}
  .leaderboard .btn{position:absolute;right:24px;bottom:6px;width:92px;height:16px;font-size:11px;line-height:16px}

  /* large rectangle 300x600 */
  .large-rect{width:240px;height:480px;left:calc(74px + var(--i)*24px);top:calc(370px + var(--i)*24px)}
  .large-rect .brand-cell{left:4px;top:3px;width:232px;height:58px;border-top:3px solid var(--gold-line);display:flex;flex-direction:column;align-items:center;justify-content:center}
  .large-rect .brand{font-size:30px}
  .large-rect .brand small{display:block;font-size:11px;color:var(--gold-ink);margin-top:2px;letter-spacing:.1em}
  .large-rect .photo{left:4px;top:63px;width:232px;height:222px}
  .large-rect .copy{left:4px;top:290px;width:232px;height:130px;border-top:4px solid var(--gold-line);border-bottom:3px solid var(--gold-line)}
  .large-rect .headline{position:absolute;left:10px;top:18px;font-size:24px;letter-spacing:.03em}
  .large-rect .btn{position:absolute;left:46px;top:82px;width:144px;height:28px;font-size:15px;line-height:28px}
  .large-rect .url{left:0;top:438px;width:240px;text-align:center;font-size:18px}

  /* wide skyscraper 160x600 */
  .skyscraper{width:129px;height:480px;left:calc(481px + var(--i)*24px);top:calc(428px + var(--i)*24px)}
  .skyscraper .brand-cell{left:3px;top:4px;width:123px;height:92px;border-top:3px solid var(--gold-line);display:flex;flex-direction:column;align-items:center;justify-content:center}
  .skyscraper .brand{font-size:19px}
  .skyscraper .brand small{display:block;font-size:9px;color:var(--gold-ink);margin-top:2px;letter-spacing:.1em}
  .skyscraper .photo{left:3px;top:100px;width:123px;height:136px}
  .skyscraper .copy{left:3px;top:240px;width:123px;height:192px;border-top:4px solid var(--gold-line);border-bottom:3px solid var(--gold-line)}
  .skyscraper .headline{position:absolute;left:8px;top:22px;font-size:30px;line-height:1.05}
  .skyscraper .headline .lead{font-size:21px;letter-spacing:.04em;display:block;margin-bottom:2px}
  .skyscraper .btn{position:absolute;left:22px;top:142px;width:84px;height:19px;font-size:11px;line-height:19px}
  .skyscraper .url{left:0;top:450px;width:129px;text-align:center;font-size:10px}

  /* medium rectangle 300x250 */
  .medium-rect{width:240px;height:200px;left:calc(776px + var(--i)*24px);top:calc(489px + var(--i)*24px)}
  .medium-rect .photo{left:3px;top:3px;width:234px;height:160px}
  .medium-rect .headline{left:10px;top:130px;font-size:17px;font-weight:700;color:#fff;text-shadow:0 1px 3px rgba(0,0,0,.45);white-space:nowrap}
  .medium-rect .btn{left:139px;top:152px;width:78px;height:16px;font-size:10px;line-height:16px}
  .medium-rect .foot{left:3px;top:165px;width:234px;height:32px;display:flex;align-items:center;justify-content:space-between;padding:0 8px 0 10px}
  .medium-rect .brand{font-size:17px}
  .medium-rect .url{font-size:9.5px}

  /* mobile leaderboard 320x50 */
  .mobile{width:256px;height:40px;left:calc(762px + var(--i)*24px);top:calc(848px + var(--i)*24px)}
  .mobile .brand-cell{left:3px;top:3px;width:54px;height:34px;display:flex;align-items:flex-end;justify-content:center;padding-bottom:3px}
  .mobile .brand{font-size:7px;letter-spacing:0}
  .mobile .photo{left:57px;top:3px;width:70px;height:34px}
  .mobile .copy{left:127px;top:3px;width:122px;height:34px}
  .mobile .headline{position:absolute;left:8px;top:3px;width:70px;font-size:10px;line-height:1.1}
  .mobile .btn{position:absolute;right:6px;top:22px;width:44px;height:10px;font-size:7px;line-height:10px}
</style>
</head>
<body>

<section class="set set-leaderboard" aria-label="Leaderboard 728x90">
  <div class="ad leaderboard v1"><div class="brand-cell panel"><span class="brand">Valmira</span></div><div class="photo" role="img" aria-label="Older woman doing a yoga pose on a lakeside beach"></div><div class="accent"></div><div class="copy panel"><p class="headline">The Future of Aging is Here</p><p class="url">https://valmiraliving.example/</p><span class="btn">Learn more</span></div></div>
  <div class="ad leaderboard v2"><div class="brand-cell panel"><span class="brand">Valmira</span></div><div class="photo" role="img" aria-label="Caregiver holding a senior's hands"></div><div class="accent"></div><div class="copy panel"><p class="headline">Idaho's New Senior Care Option</p><p class="url">https://valmiraliving.example/</p><span class="btn">Learn more</span></div></div>
  <div class="ad leaderboard v3"><div class="brand-cell panel"><span class="brand">Valmira</span></div><div class="photo" role="img" aria-label="Warm, cosy home interior"></div><div class="accent"></div><div class="copy panel"><p class="headline">The Future of Aging is Here</p><p class="url">https://valmiraliving.example/</p><span class="btn">Learn more</span></div></div>
  <div class="ad leaderboard v4"><div class="brand-cell panel"><span class="brand">Valmira</span></div><div class="photo" role="img" aria-label="Senior relaxing at home with a dog"></div><div class="accent"></div><div class="copy panel"><p class="headline">The Future of Aging is Here</p><p class="url">https://valmiraliving.example/</p><span class="btn">Learn more</span></div></div>
  <div class="ad leaderboard v5"><div class="brand-cell panel"><span class="brand">Valmira</span></div><div class="photo" role="img" aria-label="Close-up of caring hands"></div><div class="accent"></div><div class="copy panel"><p class="headline">Dementia At-Home Care</p><p class="url">https://valmiraliving.example/</p><span class="btn">Learn more</span></div></div>
  <div class="ad leaderboard v6"><div class="brand-cell panel"><span class="brand">Valmira</span></div><div class="photo" role="img" aria-label="Blue lake with forested shoreline"></div><div class="accent"></div><div class="copy panel"><p class="headline">Idaho's New Senior Care Option</p><p class="url">https://valmiraliving.example/</p><span class="btn">Learn more</span></div></div>
</section>

<section class="set set-large-rect" aria-label="Large rectangle 300x600">
  <div class="ad large-rect v1"><div class="brand-cell panel"><span class="brand">VALMIRA<small>Living</small></span></div><div class="photo" role="img" aria-label="Older woman doing a yoga pose on a lakeside beach"></div><div class="copy panel"><p class="headline">The Future of Aging is Here</p><span class="btn">Learn more</span></div><p class="url">https://valmiraliving.example/</p></div>
  <div class="ad large-rect v2"><div class="brand-cell panel"><span class="brand">VALMIRA<small>Living</small></span></div><div class="photo" role="img" aria-label="Caregiver holding a senior's hands"></div><div class="copy panel"><p class="headline">Idaho's New Senior Care Option</p><span class="btn">Learn more</span></div><p class="url">https://valmiraliving.example/</p></div>
  <div class="ad large-rect v3"><div class="brand-cell panel"><span class="brand">VALMIRA<small>Living</small></span></div><div class="photo" role="img" aria-label="Warm, cosy home interior"></div><div class="copy panel"><p class="headline">Dementia At-Home Care</p><span class="btn">Learn more</span></div><p class="url">https://valmiraliving.example/</p></div>
  <div class="ad large-rect v4"><div class="brand-cell panel"><span class="brand">VALMIRA<small>Living</small></span></div><div class="photo" role="img" aria-label="Senior relaxing at home with a dog"></div><div class="copy panel"><p class="headline">The Future of Aging is Here</p><span class="btn">Learn more</span></div><p class="url">https://valmiraliving.example/</p></div>
  <div class="ad large-rect v5"><div class="brand-cell panel"><span class="brand">VALMIRA<small>Living</small></span></div><div class="photo" role="img" aria-label="Close-up of caring hands"></div><div class="copy panel"><p class="headline">The Future of Aging is Here</p><span class="btn">Learn more</span></div><p class="url">https://valmiraliving.example/</p></div>
  <div class="ad large-rect v6"><div class="brand-cell panel"><span class="brand">VALMIRA<small>Living</small></span></div><div class="photo" role="img" aria-label="Blue lake with forested shoreline"></div><div class="copy panel"><p class="headline">Idaho's New Senior Care Option</p><span class="btn">Learn more</span></div><p class="url">https://valmiraliving.example/</p></div>
</section>

<section class="set set-skyscraper" aria-label="Wide skyscraper 160x600">
  <div class="ad skyscraper v1"><div class="brand-cell panel"><span class="brand">VALMIRA<small>Living</small></span></div><div class="photo" role="img" aria-label="Older woman doing a yoga pose on a lakeside beach"></div><div class="copy panel"><p class="headline"><span class="lead">The Future</span>of Aging is Here</p><span class="btn">Learn more</span></div><p class="url">https://valmiraliving.example/</p></div>
  <div class="ad skyscraper v2"><div class="brand-cell panel"><span class="brand">VALMIRA<small>Living</small></span></div><div class="photo" role="img" aria-label="Caregiver holding a senior's hands"></div><div class="copy panel"><p class="headline"><span class="lead">Idaho's New</span>Senior Care Option</p><span class="btn">Learn more</span></div><p class="url">https://valmiraliving.example/</p></div>
  <div class="ad skyscraper v3"><div class="brand-cell panel"><span class="brand">VALMIRA<small>Living</small></span></div><div class="photo" role="img" aria-label="Warm, cosy home interior"></div><div class="copy panel"><p class="headline"><span class="lead">The Future</span>of Aging is Here</p><span class="btn">Learn more</span></div><p class="url">https://valmiraliving.example/</p></div>
  <div class="ad skyscraper v4"><div class="brand-cell panel"><span class="brand">VALMIRA<small>Living</small></span></div><div class="photo" role="img" aria-label="Senior relaxing at home with a dog"></div><div class="copy panel"><p class="headline"><span class="lead">Dementia</span>At-Home Care</p><span class="btn">Learn more</span></div><p class="url">https://valmiraliving.example/</p></div>
  <div class="ad skyscraper v5"><div class="brand-cell panel"><span class="brand">VALMIRA<small>Living</small></span></div><div class="photo" role="img" aria-label="Close-up of caring hands"></div><div class="copy panel"><p class="headline"><span class="lead">The Future</span>of Aging is Here</p><span class="btn">Learn more</span></div><p class="url">https://valmiraliving.example/</p></div>
  <div class="ad skyscraper v6"><div class="brand-cell panel"><span class="brand">VALMIRA<small>Living</small></span></div><div class="photo" role="img" aria-label="Blue lake with forested shoreline"></div><div class="copy panel"><p class="headline"><span class="lead">Idaho's New</span>Care Option</p><span class="btn">Learn more</span></div><p class="url">https://valmiraliving.example/</p></div>
</section>

<section class="set set-medium-rect" aria-label="Medium rectangle 300x250">
  <div class="ad medium-rect v1"><div class="photo" role="img" aria-label="Older woman doing a yoga pose on a lakeside beach"></div><p class="headline">The Future of Aging is Here</p><span class="btn">Check Details</span><div class="foot panel"><span class="brand">VALMIRA</span><span class="url">https://valmiraliving.example/</span></div></div>
  <div class="ad medium-rect v2"><div class="photo" role="img" aria-label="Caregiver holding a senior's hands"></div><p class="headline">Senior Care Option</p><span class="btn">Check Details</span><div class="foot panel"><span class="brand">VALMIRA</span><span class="url">https://valmiraliving.example/</span></div></div>
  <div class="ad medium-rect v3"><div class="photo" role="img" aria-label="Warm, cosy home interior"></div><p class="headline">Aging is Here</p><span class="btn">Check Details</span><div class="foot panel"><span class="brand">VALMIRA</span><span class="url">https://valmiraliving.example/</span></div></div>
  <div class="ad medium-rect v4"><div class="photo" role="img" aria-label="Senior relaxing at home with a dog"></div><p class="headline">Aging is Here</p><span class="btn">Check Details</span><div class="foot panel"><span class="brand">VALMIRA</span><span class="url">https://valmiraliving.example/</span></div></div>
  <div class="ad medium-rect v5"><div class="photo" role="img" aria-label="Close-up of caring hands"></div><p class="headline">At-Home Care</p><span class="btn">Check Details</span><div class="foot panel"><span class="brand">VALMIRA</span><span class="url">https://valmiraliving.example/</span></div></div>
  <div class="ad medium-rect v6"><div class="photo" role="img" aria-label="Blue lake with forested shoreline"></div><p class="headline">Care Option</p><span class="btn">Check Details</span><div class="foot panel"><span class="brand">VALMIRA</span><span class="url">https://valmiraliving.example/</span></div></div>
</section>

<section class="set set-mobile" aria-label="Mobile leaderboard 320x50">
  <div class="ad mobile v1"><div class="brand-cell panel"><span class="brand">Valmira Living</span></div><div class="photo" role="img" aria-label="Older woman doing a yoga pose on a lakeside beach"></div><div class="copy panel"><p class="headline">The Future of Aging is Here</p><span class="btn">Learn more</span></div></div>
  <div class="ad mobile v2"><div class="brand-cell panel"><span class="brand">Valmira Living</span></div><div class="photo" role="img" aria-label="Caregiver holding a senior's hands"></div><div class="copy panel"><p class="headline">Senior Care Option</p><span class="btn">Learn more</span></div></div>
  <div class="ad mobile v3"><div class="brand-cell panel"><span class="brand">Valmira Living</span></div><div class="photo" role="img" aria-label="Warm, cosy home interior"></div><div class="copy panel"><p class="headline">Aging is Here</p><span class="btn">Learn more</span></div></div>
  <div class="ad mobile v4"><div class="brand-cell panel"><span class="brand">Valmira Living</span></div><div class="photo" role="img" aria-label="Senior relaxing at home with a dog"></div><div class="copy panel"><p class="headline">Aging is Here</p><span class="btn">Learn more</span></div></div>
  <div class="ad mobile v5"><div class="brand-cell panel"><span class="brand">Valmira Living</span></div><div class="photo" role="img" aria-label="Close-up of caring hands"></div><div class="copy panel"><p class="headline">Home Care</p><span class="btn">Learn more</span></div></div>
  <div class="ad mobile v6"><div class="brand-cell panel"><span class="brand">Valmira Living</span></div><div class="photo" role="img" aria-label="Blue lake with forested shoreline"></div><div class="copy panel"><p class="headline">Senior Care Option</p><span class="btn">Learn more</span></div></div>
</section>

</body>
</html>
```